Website incl. html for real estate project

We need the design and implementation of a website for a real estate project. Condominiums are built, which are sold.
We upload the sales brochure. The website should be based on the design of the sales brochure.
There are three houses with 5 apartments each. It should be rendered like this. The structure of the menu should be roughly as follows. Most information about the content is either in the appendix as a picture or in the brochure (PDF)):
Home (page 4-5 from the brochure)
House A
house B
house c
overview
basement
Municipal elections (page 6-7 in the brochure pdf)
Contact
Please use Roboto Regular as font.
And one page should give an overview of all apartments with the prices, the living space, etc. as on the file overview2.jpg.
If you go to the House A, House B, or House C menus, a page should come up with the details for that house only. The pages in the brochure are:
House A (Page 10-11)
House B (page 22-23)
House C (page 34-35)
The individual apartments should each be shown on a property page. There the plan / floor plan of the apartment and the pictures from the inside should be shown. As with the object page.jpg attachment.
Für die Designer... Mehr Zeit...
Coded - Design and coding required
1 page

```html
<!DOCTYPE html>
<html lang="de">
<head>
<meta charset="utf-8">
<title>Wohnpark am Ahorn – Halden Immobilien AG</title>
<link rel="stylesheet" href="https://fonts.googleapis.com/css2?family=Roboto:wght@400;500;700;900&family=Roboto+Condensed:wght@700&display=swap">
<style>
:root{
  --blue:#0d6993;
  --blue-dark:#0b5c82;
  --red:#e30613;
  --text:#4a4a4a;
  --muted:#777;
  --field:#f1f1f1;
  --white:#fff;
}
*{box-sizing:border-box;margin:0;padding:0}
html,body{width:1200px;height:3157px;overflow:hidden;background:var(--white)}
body{position:relative;font-family:Roboto,Arial,sans-serif;color:var(--text)}
.abs{position:absolute}

/* top bar */
.topbar{left:527px;top:0;width:673px;height:34px;background:var(--blue);clip-path:polygon(26px 0,100% 0,100% 100%,0 100%);color:var(--white);font-size:13px;font-weight:500}
.topbar span{position:absolute;top:9px;display:flex;align-items:center;gap:6px}
.topbar .sep{position:absolute;top:9px;width:1px;height:17px;background:rgba(255,255,255,.5)}
.topbar .soc{position:absolute;top:10px;width:13px;height:13px;border:1.6px solid var(--white);border-radius:3px}

/* header */
.brand{left:88px;top:48px;width:212px;color:var(--blue);font-weight:500;line-height:1}
.brand .name{font-size:30px;letter-spacing:1.5px}
.brand .sub{font-size:14px;letter-spacing:5px;color:var(--red);margin-top:6px;padding-left:30px}
.nav{top:70px;left:365px;display:flex;gap:28.5px;font-size:13px;font-weight:500;color:#333}

/* hero */
.hero{left:0;top:124px;width:1200px;height:641px;background:linear-gradient(180deg,#cfd9e2 0%,#e3e8ea 30%,#a9aea6 50%,#55773a 62%,#3f6a25 85%,#2f5a1b 100%)}
.hero-title{left:0;width:1200px;top:390px;text-align:center;color:var(--white);font-family:'Roboto Condensed',Roboto,sans-serif;font-size:112px;letter-spacing:2px;line-height:1}
.hero-sub{left:0;width:1200px;top:512px;text-align:center;color:var(--white);font-family:'Roboto Condensed',Roboto,sans-serif;font-size:36px;line-height:1}
.hero-inset{left:1000px;top:666px;width:200px;height:198px;border:4px solid var(--white);background:linear-gradient(180deg,#cfe0ef 0%,#dfe4e6 45%,#8ea27a 70%,#5d7f42 100%)}

/* section heading */
.sec-title{left:0;width:1200px;text-align:center;color:var(--blue);font-family:'Roboto Condensed',Roboto,sans-serif;font-size:46px;line-height:1}
.sec-line{left:575px;width:50px;height:2px;background:#c9dbe6}

/* feature lists */
.features{list-style:none;font-size:14.6px;line-height:20.5px;color:#555}
.features li{position:relative;padding-left:16px;margin-bottom:17px}
.features li svg{position:absolute;left:0;top:5px}

/* stats */
.stat{width:196px;height:142px}
.stat svg{position:absolute;left:0;top:0}
.stat .num{position:absolute;left:0;width:180px;top:44px;text-align:center;color:var(--blue);font-family:'Roboto Condensed',Roboto,sans-serif;font-size:40px;line-height:1}
.stat .lbl{position:absolute;left:0;width:180px;top:96px;text-align:center;font-size:13px;line-height:16px;color:#555}

/* gallery */
.photo{top:1650px;height:369px}

/* contact */
.map{left:144px;top:2219px;width:362px;height:362px;border-radius:50%;background:radial-gradient(circle at 50% 45%,#f2f2f2 0%,#e2e2e2 60%,#d4d4d4 100%)}
.label{font-size:11px;font-weight:700;color:#222;letter-spacing:.2px}
.label b{color:var(--red)}
.field{background:var(--field);font-size:13px;color:#888;padding:0 15px;display:flex;align-items:center}
.submit{left:562px;top:2530px;width:491px;height:47px;background:var(--red);color:var(--white);font-family:'Roboto Condensed',Roboto,sans-serif;font-size:19px;display:flex;align-items:center;justify-content:center}
.submit svg{position:absolute;right:18px;top:15px}

/* footer */
.footer{left:0;top:2731px;width:1200px;height:426px;background:var(--blue);color:var(--white)}
.f-brand{left:86px;top:2895px;width:270px;color:var(--white);font-weight:500;line-height:1}
.f-brand .name{font-size:37px;letter-spacing:2px}
.f-brand .sub{font-size:17px;letter-spacing:6px;margin-top:8px;padding-left:38px}
.f-soc{width:44px;height:44px;border-radius:50%;background:rgba(255,255,255,.12);top:2978px}
.f-soc i{position:absolute;left:15px;top:15px;width:14px;height:14px;border-radius:50%;background:var(--white)}
.f-head{font-family:'Roboto Condensed',Roboto,sans-serif;font-size:18px;color:var(--white)}
.f-links{left:427px;top:2862px;list-style:none;font-size:12.5px;font-weight:500;line-height:26.8px}
.f-info{font-size:12.5px;font-weight:500;line-height:18px}
.f-info svg{position:absolute;left:0;top:2px}
.news-input{left:851px;top:2912px;width:220px;height:43px;background:var(--white);font-size:12.5px;color:#999;padding-left:33px;display:flex;align-items:center}
.news-btn{left:1071px;top:2912px;width:40px;height:43px;background:#1a86c4}
.f-rule{left:88px;top:3101px;width:1024px;height:1px;background:rgba(255,255,255,.25)}
.copy{left:0;top:3122px;width:1200px;text-align:center;font-size:12.5px;font-weight:700}
.to-top{left:1135px;top:3079px;width:40px;height:40px;border-radius:50%;background:var(--white)}
</style>
</head>
<body>

<!-- top bar -->
<div class="abs topbar">
  <span style="left:40px">
    <svg width="12" height="12" viewBox="0 0 24 24"><path fill="#fff" d="M6.6 10.8a15 15 0 0 0 6.6 6.6l2.2-2.2a1 1 0 0 1 1-.25 11.4 11.4 0 0 0 3.6.57 1 1 0 0 1 1 1V20a1 1 0 0 1-1 1A17 17 0 0 1 3 4a1 1 0 0 1 1-1h3.5a1 1 0 0 1 1 1 11.4 11.4 0 0 0 .57 3.6 1 1 0 0 1-.25 1z"/></svg>
    Tel. +123 456 789</span>
  <div class="sep" style="left:187px"></div>
  <span style="left:208px">
    <svg width="13" height="10" viewBox="0 0 26 20"><rect width="26" height="20" rx="2" fill="#fff"/><path d="M1 2l12 9 12-9" stroke="#0d6993" stroke-width="2.4" fill="none"/></svg>
    info@wohnpark-am-ahorn.example</span>
  <div class="soc" style="left:519px"></div>
  <div class="sep" style="left:550px"></div>
  <div class="soc" style="left:568px;border-radius:4px"></div>
</div>

<!-- header -->
<div class="abs brand"><div class="name">HALDEN</div><div class="sub">IMMOBILIEN AG</div></div>
<nav class="abs nav">
  <span>STARTSEITE</span><span>HAUS A</span><span>HAUS B</span><span>HAUS C</span><span>OVERVIEW</span><span>BASEMENT</span><span>MUNICIPAL ELECTIONS</span><span>KONTAKT</span>
</nav>

<!-- hero -->
<div class="abs hero" role="img" aria-label="Visualisierung der drei Mehrfamilienhäuser mit Rasenfläche im Vordergrund"></div>
<div class="abs hero-title">HALDEN</div>
<div class="abs hero-sub">WOHNPARK AM AHORN</div>
<div class="abs hero-inset" role="img" aria-label="Aussenansicht der Wohnanlage mit Garten und Sitzplätzen"></div>

<!-- intro -->
<h1 class="abs sec-title" style="top:889px">WOHNPARK AM AHORN</h1>
<div class="abs sec-line" style="top:944px"></div>

<ul class="abs features" style="left:150px;top:985px;width:425px">
  <li><svg width="11" height="11" viewBox="0 0 12 12"><circle cx="6" cy="6" r="6" fill="#1a86c4"/><path d="M3.3 6.2l1.8 1.8 3.6-3.8" stroke="#fff" stroke-width="1.6" fill="none"/></svg>Die Überbauung mit drei Mehrfamilienhäusern und insgesamt15 Eigentumswohnungen entsteht zwischen der Brunnaustrasse und dem Sonnmattweg in Talwil bei Brunnau.</li>
  <li><svg width="11" height="11" viewBox="0 0 12 12"><circle cx="6" cy="6" r="6" fill="#1a86c4"/><path d="M3.3 6.2l1.8 1.8 3.6-3.8" stroke="#fff" stroke-width="1.6" fill="none"/></svg>Die modernen und hochwertigen Wohnungen sind gegen das ruhige Quartier Sonnmatt und den wunderschönen Ausblick auf den grünen «Tannenkopf» ausgerichtet.</li>
  <li><svg width="11" height="11" viewBox="0 0 12 12"><circle cx="6" cy="6" r="6" fill="#1a86c4"/><path d="M3.3 6.2l1.8 1.8 3.6-3.8" stroke="#fff" stroke-width="1.6" fill="none"/></svg>Die Wohnungen befinden sich an idealer Lage in Talwil mit guter Besonnung und die nächste Bushaltestelle ist nur knapp 120 Meter entfernt. Die Wohnungen sind im Obergeschoss mit grosszügigem Balkon und im Erdgeschoss mit einem gedecktem Sitzplatz und eigenem Garten ausgestattet.</li>
  <li><svg width="11" height="11" viewBox="0 0 12 12"><circle cx="6" cy="6" r="6" fill="#1a86c4"/><path d="M3.3 6.2l1.8 1.8 3.6-3.8" stroke="#fff" stroke-width="1.6" fill="none"/></svg>Der Wohnpark verfügt über ein grosszügiges, gemeinsames Parkhaus, von dem aus in jedes Gebäude ein Lift auf die gewünschte Etage führt. Jede Wohnung verfügt über einen eigenen Keller / eineigenes Kellerabteil. Zudem ist im Keller ein Schutzraum für die Bewohner vorhanden.</li>
</ul>

<ul class="abs features" style="left:615px;top:985px;width:432px">
  <li><svg width="11" height="11" viewBox="0 0 12 12"><circle cx="6" cy="6" r="6" fill="#1a86c4"/><path d="M3.3 6.2l1.8 1.8 3.6-3.8" stroke="#fff" stroke-width="1.6" fill="none"/></svg>Das Gebäude wird mit 18 bis 30 cm atmungsaktiver Steinwolle isoliert. Geheizt wird über eine moderne Wärmepumpe im Verbund mit einer Photovoltaikanlage, ökologisch hocheffizient mit zeitgemässer Technologie, unabhängig von steigenden Gas und Ölpreisen.</li>
  <li><svg width="11" height="11" viewBox="0 0 12 12"><circle cx="6" cy="6" r="6" fill="#1a86c4"/><path d="M3.3 6.2l1.8 1.8 3.6-3.8" stroke="#fff" stroke-width="1.6" fill="none"/></svg>Alle Wohnungen besitzen einen grosszügigen Wohn-, Koch-/ Essbereich mit raumhohen Fenstern verglast, was für eine helle und freundliche Atmosphäre sorgt.</li>
  <li><svg width="11" height="11" viewBox="0 0 12 12"><circle cx="6" cy="6" r="6" fill="#1a86c4"/><path d="M3.3 6.2l1.8 1.8 3.6-3.8" stroke="#fff" stroke-width="1.6" fill="none"/></svg>Die Umgebungsgestaltung passt perfekt in die ruhige, natürliche und trotzdem moderne Umgebung. Die grosszügigen Grünflächen der Erdgeschosswohnungen und die dezente Grundbepflanzung verbunden mit den Wegen runden die moderne und zeitlose Architektur des Gebäudes ab.</li>
  <li><svg width="11" height="11" viewBox="0 0 12 12"><circle cx="6" cy="6" r="6" fill="#1a86c4"/><path d="M3.3 6.2l1.8 1.8 3.6-3.8" stroke="#fff" stroke-width="1.6" fill="none"/></svg>Die Wohnungen werden schlüsselfertig zum Fixpreis abgegeben. Es besteht darüber hinaus die Möglichkeit den Innenausbau nach eigenen Wünschen in verschiedenen Bereichen massgeblich mitzugestalten.</li>
</ul>

<!-- stats -->
<div class="abs stat" style="left:88px;top:1433px">
  <svg width="196" height="142" viewBox="0 0 196 142"><path d="M2 70 L60 2 L194 60 L194 140 L160 140" fill="none" stroke="var(--blue)" stroke-width="4"/></svg>
  <div class="num">3</div><div class="lbl">Gebäude mit individuellem<br>Wohnangebot</div>
</div>
<div class="abs stat" style="left:295px;top:1433px">
  <svg width="196" height="142" viewBox="0 0 196 142"><path d="M2 70 L60 2 L194 60 L194 140 L160 140" fill="none" stroke="var(--blue)" stroke-width="4"/></svg>
  <div class="num" style="left:4px">9</div><div class="lbl" style="left:4px">unterschiedliche<br>Grundrisstypen</div>
</div>
<div class="abs stat" style="left:502px;top:1433px">
  <svg width="196" height="142" viewBox="0 0 196 142"><path d="M2 70 L60 2 L194 60 L194 140 L160 140" fill="none" stroke="var(--blue)" stroke-width="4"/></svg>
  <div class="num">27</div><div class="lbl">Parkplätze in der<br>Tiefgarage</div>
</div>
<div class="abs stat" style="left:709px;top:1433px">
  <svg width="196" height="142" viewBox="0 0 196 142"><path d="M2 70 L60 2 L194 60 L194 140 L160 140" fill="none" stroke="var(--blue)" stroke-width="4"/></svg>
  <div class="num">15</div><div class="lbl">komfortable<br>Wohnungen</div>
</div>
<div class="abs stat" style="left:916px;top:1433px">
  <svg width="196" height="142" viewBox="0 0 196 142"><path d="M2 70 L60 2 L194 60 L194 140 L160 140" fill="none" stroke="var(--blue)" stroke-width="4"/></svg>
  <div class="num">120</div><div class="lbl">Meter bis zur<br>Bushaltestelle</div>
</div>

<!-- gallery -->
<div class="abs photo" style="left:88px;width:211px;background:linear-gradient(180deg,#eceae6 0%,#e2dfda 60%,#d3d0cb 100%)" role="img" aria-label="Badezimmer mit rundem Spiegel und weissem Waschtisch"></div>
<div class="abs photo" style="left:308px;width:583px;background:linear-gradient(180deg,#efefed 0%,#e4e3e0 55%,#bdbab5 100%)" role="img" aria-label="Offener Wohn- und Essbereich mit Esstisch und Sofa"></div>
<div class="abs photo" style="left:900px;width:211px;background:linear-gradient(90deg,#c9b9a4 0%,#e9e7e4 35%,#dedcd8 100%)" role="img" aria-label="Kinderzimmer mit Schreibtisch und Bett"></div>

<!-- contact -->
<h2 class="abs sec-title" style="top:2118px">KONTAKT HALDEN</h2>
<div class="abs sec-line" style="top:2172px"></div>

<div class="abs map" role="img" aria-label="Umgebungskarte mit Standortmarkierung"></div>

<div class="abs label" style="left:561px;top:2221px">FIRST NAME<b>*</b></div>
<div class="abs label" style="left:810px;top:2221px">LAST NAME<b>*</b></div>
<div class="abs field" style="left:562px;top:2239px;width:242px;height:41px">Enter first name</div>
<div class="abs field" style="left:810px;top:2239px;width:243px;height:41px">Enter last name</div>

<div class="abs label" style="left:561px;top:2297px">EMAIL<b>*</b></div>
<div class="abs label" style="left:810px;top:2297px">PHONE<b>*</b></div>
<div class="abs field" style="left:562px;top:2315px;width:242px;height:41px">Enter your email</div>
<div class="abs field" style="left:810px;top:2315px;width:243px;height:41px">Enter phone number</div>

<div class="abs label" style="left:561px;top:2373px">MESSAGE<b>*</b></div>
<div class="abs field" style="left:562px;top:2390px;width:491px;height:112px;align-items:flex-start;padding-top:20px">Type your text...</div>

<div class="abs submit">SUBMIT NOW
  <svg width="18" height="18" viewBox="0 0 24 24"><path fill="#fff" d="M23 1L1 11l7 3 2 8 4-6 6 4z"/></svg>
</div>

<!-- footer -->
<footer class="abs footer"></footer>
<div class="abs f-brand"><div class="name">HALDEN</div><div class="sub">IMMOBILIEN AG</div></div>
<div class="abs f-soc" style="left:120px"><i></i></div>
<div class="abs f-soc" style="left:173px"><i></i></div>
<div class="abs f-soc" style="left:226px"><i></i></div>
<div class="abs f-soc" style="left:277px"><i></i></div>

<div class="abs f-head" style="left:427px;top:2815px">QUICK LINKS</div>
<ul class="abs f-links">
  <li>Startseite</li><li>Haus A</li><li>Haus B</li><li>Haus C</li><li>Overview</li><li>Basement</li><li>Municipal elections</li><li>Kontakt</li>
</ul>

<div class="abs f-head" style="left:606px;top:2815px">CONTACT INFO</div>
<div class="abs f-info" style="left:606px;top:2856px;padding-left:23px;width:240px">
  <svg width="13" height="10" viewBox="0 0 26 20"><rect width="26" height="20" rx="2" fill="#fff"/><path d="M1 2l12 9 12-9" stroke="#0d6993" stroke-width="2.4" fill="none"/></svg>
  Email:<br>info@wohnpark-am-ahorn.example</div>
<div class="abs f-info" style="left:606px;top:2920px;padding-left:23px">
  <svg width="14" height="14" viewBox="0 0 24 24"><path fill="#fff" d="M6.6 10.8a15 15 0 0 0 6.6 6.6l2.2-2.2a1 1 0 0 1 1-.25 11.4 11.4 0 0 0 3.6.57 1 1 0 0 1 1 1V20a1 1 0 0 1-1 1A17 17 0 0 1 3 4a1 1 0 0 1 1-1h3.5a1 1 0 0 1 1 1 11.4 11.4 0 0 0 .57 3.6 1 1 0 0 1-.25 1z"/></svg>
  Phone:<br>+08 123-456-789</div>
<div class="abs f-info" style="left:606px;top:2982px;padding-left:23px">
  <svg width="11" height="15" viewBox="0 0 16 22"><path fill="#fff" d="M8 0a8 8 0 0 0-8 8c0 6 8 14 8 14s8-8 8-14a8 8 0 0 0-8-8zm0 11a3 3 0 1 1 0-6 3 3 0 0 1 0 6z"/></svg>
  Location:<br>Halden Immobilien AG<br>Feldweg 12<br>4300 Talwil</div>

<div class="abs f-head" style="left:851px;top:2817px">NEWSLETTER</div>
<div class="abs f-info" style="left:851px;top:2861px;width:230px;font-size:12px">Subscribe to our email address to get the latest news.</div>
<div class="abs news-input">
  <svg style="position:absolute;left:13px;top:17px" width="12" height="9" viewBox="0 0 26 20"><rect width="26" height="20" rx="2" fill="#bbb"/><path d="M1 2l12 9 12-9" stroke="#fff" stroke-width="2.4" fill="none"/></svg>
  Enter Your Email...</div>
<div class="abs news-btn"><svg style="position:absolute;left:12px;top:13px" width="17" height="17" viewBox="0 0 24 24"><path fill="#fff" d="M23 1L1 11l7 3 2 8 4-6 6 4z"/></svg></div>

<div class="abs f-rule"></div>
<div class="abs copy">2022 HALDEN IMMOBILIEN AG ALL RIGHTS RESERVED</div>
<div class="abs to-top"><svg style="position:absolute;left:15px;top:16px" width="10" height="7" viewBox="0 0 10 7"><path d="M1 6l4-4 4 4" stroke="#0d6993" stroke-width="1.6" fill="none"/></svg></div>

</body>
</html>
```